Business Cards for IT Consulting Company (Managed Service Provider)

I am looking to have some business cards printed and would like some designs. We are an IT Consulting company based in Vancouver BC. I would like a nice clean and modern look to the cards. I have uploaded all the versions of my logo so parts can be used as needed. Here is a snippit from our website homepage:

Kelbrin Systems Ltd. is an IT Solutions Partner located in Vancouver BC, Canada. We offer IT solutions and support to customers in the greater Vancouver Area. With expertise in Quillara platforms, as well as Tovex and Bryn ZPL and over 12 years experience in the IT industry, Kelbrin Systems is dedicated to offering our clients top quality service and products. We take pride in the solutions we offer our customers. The greatest compliment a client can give us is to recommend our services.

Kelbrin Systems Ltd. offers a wide range of IT services from onsite service to remote support and managed service solutions. This allows clients to choose the support path that best suits their company’s needs. Supporting many different sized companies from small to enterprise level over the past 12 years Kelbrin Systems has the experience and expertise needed to ensure things run smoothly. Allowing our clients to focus on doing business.

Revolutionizing the way IT services are delivered.

Kelbrin Systems is dedicated to providing our clients with IT solutions that work and grow with them for years to come. This philosophy helps save money in the long run instead of replacing equipment constantly. Far too often IT solutions are not well thought out and while possibly solving the problem at hand, require replacement due to growth or quality within a very short time frame. Kelbrin Systems takes pride in providing solutions that will last and be able to accommodate growth without the need for replacement.

Industry/Entity Type

Information Technology

Contact Information for Business Card

Kelbrin Systems Ltd.
(Employee Name)
Eml: (Employees Email Address)
Web: kelbrinsys.me
Ph: 604-555-0142

Font styles to use
Serif
Sans Serif

Requirements
Must have
• The Company logo and company colors.
Nice to have
• - Our tag line: "Revolutionizing IT Services" or "Revolutionizing the way IT services are delivered."
• - Also I really like the idea of nature and technology together blending which is sort of where my logo came from so integrating that somehow onto the business cards would be great.

```html
<!DOCTYPE html>
<html lang="en">
<head>
<meta charset="utf-8">
<title>Kelbrin Systems Ltd. — Business Cards</title>
<link href="https://fonts.googleapis.com/css2?family=Montserrat:wght@500;600&family=Roboto:ital,wght@0,400;0,700;1,400&display=swap" rel="stylesheet">
<style>
  :root {
    --backdrop: #a9a7a8;
    --card-dark: #1c1c1d;
    --card-light: #f2f2f2;
    --brand-blue: #1e8ad0;
    --ink: #4a4a4c;
    --ink-soft: #3d3d3f;
    --tagline-light: #e4e4e4;
    --band-grey: #555557;
    --rule: #7a7a7a;
  }
  * { margin: 0; padding: 0; box-sizing: border-box; }
  html, body {
    width: 1200px; height: 1200px; overflow: hidden;
    background: var(--backdrop);
  }
  .canvas { position: relative; width: 1200px; height: 1200px; }

  .card { position: absolute; width: 713px; height: 418px; overflow: hidden; }
  .card--front { left: 238px; top: 118px; background: var(--card-dark); }
  .card--back  { left: 230px; top: 644px; background: var(--card-light); }

  .brand {
    position: absolute; display: flex; align-items: center; gap: 16px;
    font-family: "Montserrat", sans-serif; font-weight: 600;
    color: var(--brand-blue); white-space: nowrap;
  }
  .brand__dot { width: 34px; height: 34px; border-radius: 50%; background: var(--brand-blue); flex: none; }
  .card--front .brand { left: 110px; top: 168px; font-size: 46px; }
  .card--back .brand { left: 40px; top: 78px; font-size: 46px; }

  .tagline-bar {
    position: absolute; left: 102px; top: 378px; width: 508px;
    display: flex; align-items: center; gap: 16px;
  }
  .tagline-bar__line { flex: 1; height: 3px; background: var(--brand-blue); }
  .tagline-bar__text {
    font-family: "Montserrat", sans-serif; font-weight: 500; font-size: 18px;
    color: var(--tagline-light); white-space: nowrap;
  }

  .person { position: absolute; right: 36px; top: 196px; text-align: right; font-family: "Roboto", sans-serif; }
  .person__name { font-weight: 700; font-size: 25px; color: var(--brand-blue); line-height: 1.1; }
  .person__title { font-style: italic; font-size: 16px; color: var(--ink-soft); margin-top: 7px; }

  .divider { position: absolute; left: 38px; top: 244px; width: 482px; height: 1px; background: var(--rule); }

  .contact { position: absolute; left: 38px; top: 276px; list-style: none; font-family: "Roboto", sans-serif; font-size: 18px; color: var(--ink); }
  .contact li { display: flex; align-items: center; height: 27px; }
  .contact svg { width: 16px; height: 16px; margin-right: 19px; fill: var(--brand-blue); flex: none; }

  .slogan {
    position: absolute; right: 36px; top: 300px; text-align: right;
    font-family: "Roboto", sans-serif; font-size: 18px; line-height: 25px; color: var(--ink);
  }

  .footer-bands { position: absolute; left: 0; bottom: 0; width: 713px; height: 50px; }
</style>
</head>
<body>
<div class="canvas">

  <section class="card card--front" aria-label="Card front">
    <div class="brand"><span class="brand__dot"></span>Kelbrin Systems Ltd.</div>
    <div class="tagline-bar">
      <span class="tagline-bar__line"></span>
      <span class="tagline-bar__text">Revolutionizing IT Services</span>
      <span class="tagline-bar__line"></span>
    </div>
  </section>

  <section class="card card--back" aria-label="Card back">
    <div class="brand"><span class="brand__dot"></span>Kelbrin Systems Ltd.</div>

    <div class="person">
      <p class="person__name">Dara Whitlow</p>
      <p class="person__title">Managing Director</p>
    </div>

    <div class="divider"></div>

    <ul class="contact">
      <li>
        <svg viewBox="0 0 16 16" aria-hidden="true"><path d="M2 6c0-2 2-3 6-3s6 1 6 3v1h-3V5.5C10 5 9 4.8 8 4.8S6 5 5 5.5V7H2zM4 8h8l2 5H2z"/></svg>
        604-555-0142
      </li>
      <li>
        <svg viewBox="0 0 16 16" aria-hidden="true"><path d="M8 1a7 7 0 1 0 0 14A7 7 0 0 0 8 1zm5.9 6.3h-2.6A11 11 0 0 0 10.2 2.6a6 6 0 0 1 3.7 4.7zM8 2.3c.8 1 1.6 2.8 1.8 5H6.2c.2-2.2 1-4 1.8-5zM5.8 2.6A11 11 0 0 0 4.7 7.3H2.1a6 6 0 0 1 3.7-4.7zM2.1 8.7h2.6a11 11 0 0 0 1.1 4.7 6 6 0 0 1-3.7-4.7zM8 13.7c-.8-1-1.6-2.8-1.8-5h3.6c-.2 2.2-1 4-1.8 5zm2.2-.3a11 11 0 0 0 1.1-4.7h2.6a6 6 0 0 1-3.7 4.7z"/></svg>
        www.kelbrinsys.me
      </li>
      <li>
        <svg viewBox="0 0 16 16" aria-hidden="true"><path d="M1 3h14v10H1zm1.6 1.2L8 8.6l5.4-4.4zM2.2 5.6v6.2l3.7-3.2zm11.6 0-3.7 3 3.7 3.2zM6.8 9.4l-4.2 3.4h10.8L9.2 9.4 8 10.4z"/></svg>
        support@kelbrinsys.me
      </li>
    </ul>

    <p class="slogan">Revolutionizing the way<br>IT services are delivered</p>

    <svg class="footer-bands" viewBox="0 0 713 50" aria-hidden="true">
      <rect x="0" y="28" width="713" height="22" fill="var(--band-grey)"/>
      <polygon points="360,0 713,0 713,50 327,50" fill="var(--brand-blue)"/>
    </svg>
  </section>

</div>
</body>
</html>
```